Social Media Designs for Pet Insurance Website

We are seeking the following
Twitter Background and Header Image
Facebook Cover
Google Plus Cover (1080×608)

All designs must comply with platform requirements with regard to size and other requirements (such as the Facebook text regulations).

The overriding requirement is for all 3 designs to be CONSISTENT with our website which can be found at www.critter-cover-reviews.co.uk.

We would like the five colours from the menu boxes beneath the header on our home page to be incorporated into the designs.

The photo of the dog and cat which is used in our header should be incorporated within the design.

We have attached the photo file and our logo file.

We will want to use the twitter margins to display additional information about the website which we will supply at a later stage.

You are free to amend the colours in the logo to suit the design if you wish.

All 3 designs must contain our strap line which is "Helping UK pet owners make the right pet insurance choice" and also this list
"Keep in touch
Join the discussion
Contribute your experiences"
Updates

Have just added the copy for the left hand margin on the twitter background as a new attachment to the brief.   One idea might be to display the text in boxes to mimic the menu boxes on our home page.   Just an idea though  .. very happy to see other ideas.

Reason: Unfortunately I have been called away from the office for the last couple of days so have been unable to provide the feedback etc. I have therefore decided to extend the deadline by a day.

Target Market(s)

Most importantly the designs should have the same look as feel as the website..www.critter-cover-reviews.co.uk

Industry/Entity Type

Pet

Requirements
Must have
• See brief above
Nice to have
• See brief above
Should not have
• See brief above

```html
<!DOCTYPE html>
<html lang="en">
<head>
<meta charset="utf-8">
<title>Critter Cover Reviews UK – Facebook Cover</title>
<link rel="stylesheet" href="https://fonts.googleapis.com/css2?family=Open+Sans:wght@600;700&display=swap">
<style>
  :root {
    --sky-deep: #1c47b8;
    --sky-mid: #2f6fd8;
    --sky-light: #6fa6ec;
    --sky-haze: #a9cbf3;
    --headline-yellow: #f7c417;
    --text-white: #ffffff;
    --brand-white: #ffffff;
    --photo-gold: #d9a450;
    --photo-cream: #f0d9a8;
    --photo-shadow: #8a6a3a;
  }
  * { margin: 0; padding: 0; box-sizing: border-box; }
  html, body { width: 1200px; height: 444px; overflow: hidden; }
  body { font-family: "Open Sans", Arial, sans-serif; }

  .cover {
    position: relative;
    width: 1200px;
    height: 444px;
    overflow: hidden;
    background:
      radial-gradient(ellipse 700px 420px at 1000px 60px, var(--sky-haze) 0%, rgba(169,203,243,0) 70%),
      linear-gradient(100deg, var(--sky-deep) 0%, var(--sky-mid) 45%, var(--sky-light) 100%);
  }

  .hero-photo {
    position: absolute;
    left: 640px;
    top: 0;
    width: 560px;
    height: 444px;
    background:
      radial-gradient(ellipse 220px 200px at 240px 250px, var(--photo-cream) 0%, var(--photo-gold) 55%, rgba(217,164,80,0) 100%),
      radial-gradient(ellipse 120px 110px at 150px 90px, var(--photo-shadow) 0%, rgba(138,106,58,0) 100%);
  }

  .brand {
    position: absolute;
    left: 40px;
    top: 38px;
    display: flex;
    align-items: center;
    gap: 14px;
  }
  .brand-mark {
    width: 58px;
    height: 58px;
    border-radius: 50%;
    background: var(--brand-white);
    opacity: 0.9;
  }
  .brand-name {
    color: var(--brand-white);
    font-weight: 600;
    font-size: 27px;
    line-height: 1.05;
  }

  .strapline {
    position: absolute;
    left: 40px;
    top: 168px;
    color: var(--headline-yellow);
    font-weight: 700;
    font-size: 30px;
    line-height: 46px;
    letter-spacing: 0.2px;
    text-transform: uppercase;
  }

  .benefits {
    position: absolute;
    left: 288px;
    top: 286px;
    list-style: none;
  }
  .benefits li {
    display: flex;
    align-items: center;
    height: 49px;
    color: var(--text-white);
    font-weight: 600;
    font-size: 22.5px;
  }
  .benefits svg {
    width: 20px;
    height: 20px;
    margin-right: 14px;
    flex: none;
  }
</style>
</head>
<body>
  <main class="cover">
    <div class="hero-photo" role="img" aria-label="Photo of a smiling child hugging a golden retriever against a blue sky"></div>

    <div class="brand">
      <span class="brand-mark"></span>
      <span class="brand-name">Critter Cover<br>Reviews UK</span>
    </div>

    <h1 class="strapline">Helping UK pet owners make<br>the right pet insurance choice</h1>

    <ul class="benefits">
      <li><svg viewBox="0 0 20 20" aria-hidden="true"><path d="M3 11 L8 16 L17 4" fill="none" stroke="#ffffff" stroke-width="3" stroke-linecap="round" stroke-linejoin="round"/></svg>Keep in touch</li>
      <li><svg viewBox="0 0 20 20" aria-hidden="true"><path d="M3 11 L8 16 L17 4" fill="none" stroke="#ffffff" stroke-width="3" stroke-linecap="round" stroke-linejoin="round"/></svg>Join the discussion</li>
      <li><svg viewBox="0 0 20 20" aria-hidden="true"><path d="M3 11 L8 16 L17 4" fill="none" stroke="#ffffff" stroke-width="3" stroke-linecap="round" stroke-linejoin="round"/></svg>Contribute your experiences</li>
    </ul>
  </main>
</body>
</html>
```